依頼詳細
事務所の名刺を作成したいと考えています。名刺は自己紹介用と取り扱い業務紹介用2種類の合計3種類作成する予定ですが、まず自己紹介用名刺のデザインをお願いいたします。今回作成いただく名刺は主に同業、他士業の方へのあいさつ用として使用します。
記載項目
行政書士 office TOMURA
代表 竹下 健二
〒***-****大阪府池田市**番**号
*********** *号室
℡***-***-**** Fax:***-***-*****
Email:info@*************.com
URL:https://*************.com
希望イメージ
• シンプル
複雑
• 単色
カラフル
• 暗い
明るい
• 日常
高級
• 遊び心
厳粛
• 未来的
伝統的
• 女性的
男性的
希望する色
赤系、青系、水色系
納品ファイル
補足説明
プロフィール写真はデザイン確定後送付します。
依頼公開後の追記内容
■ 選んだ理由

とても素敵なデザインでした。
派手過ぎず、しかし事務所名をしっかり伝えることができます。
裏面の活用など自分のイメージ通りの出来でした。
本当にありがとうございました。

■ 提案者全員のお礼・コメント

たくさんのデザインを頂きました。
どのデザインもスマートで、どれを選ぶかとても悩み、悩みに悩み抜いた結果として
1点を選びました。
残念ながら選に漏れた方が多数ですが、皆様から良いデザインをご提案頂いたと思っ
ています。
応募いただいた皆様にお礼申し上げます。

```html
<!DOCTYPE html>
<html lang="ja">
<head>
<meta charset="utf-8">
<title>行政書士 office TOMURA 名刺</title>
<link rel="stylesheet" href="https://fonts.googleapis.com/css2?family=Noto+Serif+JP:wght@400;500&display=swap">
<style>
  :root {
    --page-bg: #e9e9ea;
    --card-bg: #ffffff;
    --ink: #3a3a3a;
    --ink-soft: #555555;
    --accent-red: #c8161d;
    --watermark: #f2f2f3;
  }
  html, body {
    margin: 0;
    padding: 0;
    width: 1200px;
    height: 1200px;
    overflow: hidden;
    background: var(--page-bg);
  }
  .card {
    position: absolute;
    left: 100px;
    top: 298px;
    width: 1000px;
    height: 604px;
    background: var(--card-bg);
    overflow: hidden;
    font-family: "Noto Serif JP", serif;
    color: var(--ink);
  }
  .card__backdrop {
    position: absolute;
    left: 500px;
    top: -3px;
    width: 450px;
    height: 450px;
    border-radius: 50%;
    background: var(--watermark);
  }
  .brand {
    position: absolute;
    left: 233px;
    top: 248px;
    display: flex;
    align-items: center;
    gap: 26px;
  }
  .brand__dot {
    width: 80px;
    height: 80px;
    border-radius: 50%;
    background: var(--accent-red);
    flex: none;
  }
  .brand__name {
    display: flex;
    align-items: flex-end;
    gap: 14px;
    font-weight: 400;
    color: var(--ink);
    line-height: 1;
  }
  .brand__sub {
    display: flex;
    flex-direction: column;
    gap: 6px;
  }
  .brand__title { font-size: 21px; letter-spacing: 0.12em; }
  .brand__office { font-size: 38px; }
  .brand__main { font-size: 70px; letter-spacing: 0.04em; }
  .services {
    position: absolute;
    left: 0;
    right: 0;
    top: 466px;
    text-align: center;
    color: var(--ink-soft);
    font-size: 17px;
    line-height: 1;
  }
  .services__heading { margin: 0 0 24px; font-weight: 400; font-size: 17px; letter-spacing: 0.08em; }
  .services__list { margin: 0; letter-spacing: 0.04em; }
</style>
</head>
<body>
  <div class="card">
    <div class="card__backdrop" aria-hidden="true"></div>
    <div class="brand">
      <div class="brand__dot" aria-hidden="true"></div>
      <div class="brand__name">
        <div class="brand__sub">
          <span class="brand__title">行政書士</span>
          <span class="brand__office">office</span>
        </div>
        <span class="brand__main">TOMURA</span>
      </div>
    </div>
    <div class="services">
      <h2 class="services__heading">業務内容</h2>
      <p class="services__list">外国人のビザ申請と創業融資・会社設立・融資支援、補助金支援など</p>
    </div>
  </div>
</body>
</html>
```